Sparrowgate Petals Website v.1 - attract floral shop franchisees

I need a simple information website for my new business. We are a franchisor of flower shops. The overall purpose of the website is to promote the company and the service, especially to potential franchisees and retailers. Only about 4 pages are required including homepage, About, For Supermarkets, For Franchisees, and Contact. No special functions are required except the site will have two separate inquiry forms that must be filled out online and submitted via automated email. Similarly, an email form should be linked from the Contact page. I have a logo and business cards designed by ArtQuarry, and I would like the site to have a consistent color scheme and style. The key to design will be to express the joy and love associated with flowers and floral bouquets.
IMPORTANT - I will be exporting the website design to Wordpress CMS in a site hosted by HostNimbus. For smooth integration into WordPress hosted by HostNimbus, the designer should build the site using a WordPress-friendly format. Ideally, they should use HTML, CSS, and PHP. Creating a custom theme or using a page builder that exports to WordPress-compatible files is best. This ensures the site can be easily imported and managed within WordPress.

Target Market(s)

Potential franchisees (existing florists or creative types who might like to own a floral business) and supermarkets who might want us to run their floral department

Industry/Entity Type

Floral retailing

Requirements
Must have
• A brand theme that is beautiful, consistent throughout and builds on the logo design
Nice to have
• Show gender and ethnic diversity in customers and florists. Pictures of happy florists (for franchisees) and pictures of amazing floral department displays (for supermarkets)

```html
<!DOCTYPE html>
<html lang="en">
<head>
<meta charset="utf-8">
<title>Sparrowgate Petals – Home</title>
<link href="https://fonts.googleapis.com/css2?family=Jost:wght@400;500;600&family=Oswald:wght@500&family=Yellowtail&display=swap" rel="stylesheet">
<style>
:root{
  --green:#0b8a3c;
  --orange:#f0a000;
  --ink:#222;
  --text:#333;
  --muted:#555;
  --soft:#f6f6f6;
  --line:#e3e3e3;
  --white:#fff;
}
*{box-sizing:border-box;margin:0;padding:0}
html,body{width:1200px;height:3311px;overflow:hidden}
body{position:relative;font-family:'Jost',sans-serif;color:var(--text);background:var(--white)}
section,header,footer{position:absolute;left:0;width:1200px}
.btn{position:absolute;background:var(--orange);color:var(--ink);font:500 15px 'Jost',sans-serif;display:flex;align-items:center;justify-content:center;width:127px;height:42px}
.script{font-family:'Yellowtail',cursive;font-weight:400;white-space:nowrap}
.script .o{color:var(--orange)} .script .g{color:var(--green)}
.photo{position:absolute}

/* header */
.site-header{top:0;height:110px}
.brand{position:absolute;left:141px;top:28px;display:flex;align-items:center;gap:10px}
.brand-dot{width:40px;height:40px;border-radius:50%;background:var(--orange)}
.brand-name{font:500 22px 'Jost',sans-serif;color:var(--green)}
.contact-row{position:absolute;top:7px;right:140px;display:flex;gap:26px;font-size:14px;color:var(--ink);align-items:center}
.contact-row span{display:flex;align-items:center;gap:12px}
.chip{width:32px;height:32px;border-radius:50%;background:#f3f3f3;display:flex;align-items:center;justify-content:center}
.header-rule{position:absolute;left:440px;top:57px;width:620px;height:1px;background:var(--line)}
.nav{position:absolute;top:76px;left:505px;display:flex;gap:50px;font-size:13px;color:var(--ink)}
.nav .active{color:var(--orange)}

/* hero */
.hero{top:110px;height:530px;background:linear-gradient(100deg,#4a4438 0%,#7a7062 35%,#cfc8bd 65%,#e8e2d8 100%)}
.hero h1{position:absolute;left:141px;top:132px;font:500 58px/66px 'Oswald',sans-serif;color:var(--white);letter-spacing:-1px}

/* about */
.about{top:640px;height:676px}
.frame{position:absolute;background:var(--green)}
.about p{font-size:12.6px;line-height:23px;color:var(--text)}
.about-head{position:absolute;left:585px;top:122px;font-size:42px;line-height:50px}
.about-col{position:absolute;left:587px;top:185px;width:474px}
.about-col p+p{margin-top:12px}
.about-wide{position:absolute;left:166px;top:485px;width:890px}

/* partner */
.partner{top:1316px;height:549px;background:var(--soft)}
.partner-name{position:absolute;left:141px;top:150px;font:500 18px 'Jost',sans-serif;color:var(--ink)}
.partner-text{position:absolute;left:141px;top:226px;width:470px;font-size:12.6px;line-height:23px}
.partner-text p+p{margin-top:4px}

/* reviews */
.reviews{top:1865px;height:598px}
.reviews h2{position:absolute;left:0;width:1200px;top:104px;text-align:center;font-size:42px;line-height:50px}
.card{position:absolute;width:288px;background:var(--white);border:1px solid var(--line);border-radius:4px;text-align:center}
.card.lift{box-shadow:0 4px 14px rgba(0,0,0,.12)}
.stars{margin:28px auto 0;display:flex;justify-content:center}
.card p{margin:24px 24px 0;font-size:12.4px;line-height:22px;color:var(--muted)}
.who{position:absolute;bottom:50px;left:0;right:0;display:flex;align-items:center;justify-content:center;gap:14px;font:500 15px 'Jost',sans-serif;color:var(--ink)}
.avatar{width:62px;height:62px;border-radius:50%;background:linear-gradient(135deg,#b9a79a,#6f6259)}
.arrow{position:absolute;width:36px;height:36px;border-radius:50%;display:flex;align-items:center;justify-content:center}
.arrow.prev{background:var(--white);box-shadow:0 1px 6px rgba(0,0,0,.15)}
.arrow.next{background:var(--green)}

/* gallery */
.gallery{top:2463px;height:515px;background:var(--soft)}
.gallery .photo{top:85px;width:219px;height:268px}

/* footer */
.site-footer{top:2978px;height:291px;background:var(--green);color:var(--white)}
.foot-head{position:absolute;top:52px;font-size:22px;line-height:28px;color:var(--orange)}
.quick{position:absolute;left:141px;top:88px;list-style:none;font-size:12.6px}
.quick li{height:33px}
.details{position:absolute;left:455px;top:88px;list-style:none;font-size:12.6px;line-height:18px}
.details li{display:flex;align-items:center;gap:14px;height:52px}
.details .ic{width:36px;height:36px;border-radius:50%;background:var(--white);flex:none;display:flex;align-items:center;justify-content:center}
.foot-brand{position:absolute;left:858px;top:98px;display:flex;align-items:center;gap:10px}
.foot-brand .brand-dot{width:46px;height:46px}
.foot-brand .brand-name{color:var(--white);font-size:20px}
.social{position:absolute;left:874px;top:185px;display:flex;gap:11px}
.social span{width:33px;height:33px;border-radius:50%;background:rgba(255,255,255,.18)}
.copy{position:absolute;left:0;top:3269px;width:1200px;height:42px;background:var(--orange);color:var(--ink);font-size:13.5px;display:flex;align-items:center;justify-content:center}
</style>
</head>
<body>

<header class="site-header">
  <div class="brand"><span class="brand-dot"></span><span class="brand-name">Sparrowgate Petals</span></div>
  <div class="contact-row">
    <span><i class="chip"><svg width="14" height="14" viewBox="0 0 24 24"><path fill="#0b8a3c" d="M6.6 10.8a15 15 0 0 0 6.6 6.6l2.2-2.2c.3-.3.7-.4 1-.2 1.1.4 2.3.6 3.6.6.6 0 1 .4 1 1V20c0 .6-.4 1-1 1C10.6 21 3 13.4 3 4c0-.6.4-1 1-1h3.5c.6 0 1 .4 1 1 0 1.3.2 2.5.6 3.6.1.3 0 .7-.2 1z"/></svg></i>123-456-7890</span>
    <span><i class="chip"><svg width="14" height="14" viewBox="0 0 24 24"><path fill="#0b8a3c" d="M3 5h18v14H3z"/><path fill="none" stroke="#fff" stroke-width="1.6" d="M3 6l9 7 9-7"/></svg></i>info@sparrowgatepetals.com</span>
  </div>
  <div class="header-rule"></div>
  <nav class="nav"><span class="active">Home</span><span>About Us</span><span>For Supermarkets</span><span>For Franchisees</span></nav>
</header>

<section class="hero" role="img" aria-label="Smiling florist arranging white roses in a flower shop">
  <h1>Freshest Flowers<br>Artisan Designs<br>Franchise Opportunities</h1>
  <span class="btn" style="left:141px;top:344px">Contact Us</span>
</section>

<section class="about">
  <div class="frame" style="left:141px;top:85px;width:348px;height:355px"></div>
  <div class="photo" role="img" aria-label="Shop owner standing with bouquets of roses and hydrangeas" style="left:167px;top:111px;width:348px;height:355px;background:linear-gradient(160deg,#a9b7a9,#6f7a70 55%,#c9b98a)"></div>
  <h2 class="about-head script"><span style="color:var(--ink)">About</span> <span class="o">Sparrowgate</span> <span class="g">Petals</span></h2>
  <div class="about-col">
    <p>Fresh flowers convey beauty and love, &amp; in our view should become something every person regularly enjoys. Sparrowgate Petals is an entrepreneurial company created to make top quality fresh flowers &amp; professionally-designed bouquets accessible to every consumer at affordable prices.</p>
    <p>Professional florists typically sell the finest quality stems, design the most beautiful bouquets and provide the finest customer service, but their costs – of floral products, retail spaces, labor and marketing – force them to pass high prices along to customers. Supermarket flower departments benefit from high customer footfall, economies of scale and low pricing, but their quality of stems and bouquets is typically poor, staffing is limited, and staff turnover is high which can result in inefficiency, wastage, poorly merchandised selections and limited service.</p>
  </div>
  <p class="about-wide">Sparrowgate Petals brings the best of professional florists and supermarkets together for the benefit of consumers. It supports a national network of owner-operator franchisees, who in many cases are multi-site professional florists, with comprehensive services to enhance franchise profitability. Sparrowgate Petals works with some of the country's largest and most progressive supermarkets to provide franchisee ownership and operation of their strategically important floral departments. Supermarkets find that Sparrowgate Petals is able to improve their financial outcomes, provide attentive customer service and satisfaction, and lift the quality of the entire store environment</p>
</section>

<section class="partner">
  <p class="partner-name">Northbay Group</p>
  <div class="partner-text">
    <p>Sparrowgate Petals operates in partnership with Northbay Group, the leading franchisor of sushi stations and pre-packaged fruit &amp; vegetable departments to supermarkets across the United States and United Kingdom.</p>
    <p>Sparrowgate Petals' combination of floral and supermarket franchising expertise guarantees that consumers, franchisees and supermarket partners each receive exceptional service and value.</p>
  </div>
  <span class="btn" style="left:141px;top:387px">Contact Us</span>
  <div class="frame" style="left:686px;top:84px;width:347px;height:355px"></div>
  <div class="photo" role="img" aria-label="Hands passing a plate of sushi rolls across a counter" style="left:711px;top:111px;width:348px;height:355px;background:linear-gradient(150deg,#6a5a48,#3f4a3c 50%,#2e6a40)"></div>
</section>

<section class="reviews">
  <h2 class="script"><span class="o">Customer</span> <span class="g">Reviews</span></h2>
  <div class="arrow prev" style="left:84px;top:327px"><svg width="12" height="12" viewBox="0 0 12 12"><path d="M8 2L4 6l4 4" fill="none" stroke="#0b8a3c" stroke-width="2"/></svg></div>
  <div class="arrow next" style="left:1079px;top:327px"><svg width="12" height="12" viewBox="0 0 12 12"><path d="M4 2l4 4-4 4" fill="none" stroke="#fff" stroke-width="2"/></svg></div>

  <div class="card" style="left:141px;top:189px;height:312px">
    <div class="stars"><svg width="110" height="18" viewBox="0 0 110 18"><g fill="#f0a000"><path id="st" d="M9 0l2.6 5.6 6.1.7-4.5 4.2 1.2 6L9 13.5 3.6 16.5l1.2-6L.3 6.3l6.1-.7z"/><use href="#st" x="23"/><use href="#st" x="46"/><use href="#st" x="69"/><use href="#st" x="92"/></g></svg></div>
    <p>Lorem ipsum dolor sit amet, consectetur adipiscing elit. Nunc congue malesuada aliquam. Vivamus sed tristique eros. Cras congue nisi sagittis enim...</p>
    <div class="who"><span class="avatar" role="img" aria-label="Reviewer portrait"></span>Ronan Wells</div>
  </div>
  <div class="card lift" style="left:457px;top:176px;height:339px">
    <div class="stars" style="margin-top:45px"><svg width="110" height="18" viewBox="0 0 110 18"><g fill="#f0a000"><use href="#st"/><use href="#st" x="23"/><use href="#st" x="46"/><use href="#st" x="69"/><use href="#st" x="92"/></g></svg></div>
    <p>Nunc congue malesuada aliquam. Vivamus sed tristique eros. Cras congue nisi sagittis enim laoreet euismod. Fusce efficitur ipsum vel est...</p>
    <div class="who" style="bottom:60px"><span class="avatar" role="img" aria-label="Reviewer portrait"></span>Nadia Byers</div>
  </div>
  <div class="card" style="left:771px;top:189px;height:312px">
    <div class="stars"><svg width="110" height="18" viewBox="0 0 110 18"><g fill="#f0a000"><use href="#st"/><use href="#st" x="23"/><use href="#st" x="46"/><use href="#st" x="69"/><use href="#st" x="92"/></g></svg></div>
    <p>Vivamus sed tristique eros. Cras congue nisi sagittis enim laoreet euismod. Fusce efficitur ipsum vel est suscipit aliquet. Duis et diam iaculis turpis...</p>
    <div class="who"><span class="avatar" role="img" aria-label="Reviewer portrait"></span>Sienna Marsh</div>
  </div>
</section>

<section class="gallery">
  <div class="photo" role="img" aria-label="Florist arranging a mixed bouquet" style="left:18px;background:linear-gradient(160deg,#d9d2c7,#8e7a6e 55%,#b5304a)"></div>
  <div class="photo" role="img" aria-label="Table of pink roses and white hydrangeas" style="left:254px;background:linear-gradient(160deg,#8c8f94,#c95a7d 55%,#e6e4dd)"></div>
  <div class="photo" role="img" aria-label="Smiling florist in a red sweater behind flowers" style="left:490px;background:linear-gradient(160deg,#ece8e2,#b0483f 55%,#efece6)"></div>
  <div class="photo" role="img" aria-label="Flower shop storefront with buckets of blooms" style="left:726px;background:linear-gradient(160deg,#3d3a33,#c98ea0 50%,#6b6a64)"></div>
  <div class="photo" role="img" aria-label="Shop owner holding a rose among arrangements" style="left:963px;background:linear-gradient(160deg,#5a4535,#8d6d5a 50%,#c99c95)"></div>
  <span class="btn" style="left:536px;top:388px">Contact Us</span>
</section>

<footer class="site-footer">
  <h3 class="foot-head script" style="left:141px">Quick Links</h3>
  <ul class="quick"><li>• Home</li><li>• About Us</li><li>• For Supermarkets</li><li>• For Franchisees</li><li>• Contact Us</li></ul>
  <h3 class="foot-head script" style="left:455px">Contact Details</h3>
  <ul class="details">
    <li><i class="ic"><svg width="14" height="16" viewBox="0 0 24 24"><path fill="#f0a000" d="M12 2a7 7 0 0 0-7 7c0 5 7 13 7 13s7-8 7-13a7 7 0 0 0-7-7zm0 9.5A2.5 2.5 0 1 1 12 6.5a2.5 2.5 0 0 1 0 5z"/></svg></i><span>123, Building Name, Street<br>City, State XY 123456</span></li>
    <li><i class="ic"><svg width="14" height="14" viewBox="0 0 24 24"><path fill="#f0a000" d="M6.6 10.8a15 15 0 0 0 6.6 6.6l2.2-2.2c.3-.3.7-.4 1-.2 1.1.4 2.3.6 3.6.6.6 0 1 .4 1 1V20c0 .6-.4 1-1 1C10.6 21 3 13.4 3 4c0-.6.4-1 1-1h3.5c.6 0 1 .4 1 1 0 1.3.2 2.5.6 3.6.1.3 0 .7-.2 1z"/></svg></i><span>123-456-7890</span></li>
    <li><i class="ic"><svg width="14" height="14" viewBox="0 0 24 24"><path fill="#f0a000" d="M3 5h18v14H3z"/><path fill="none" stroke="#fff" stroke-width="1.6" d="M3 6l9 7 9-7"/></svg></i><span>info@sparrowgatepetals.com</span></li>
  </ul>
  <div class="foot-brand"><span class="brand-dot"></span><span class="brand-name">Sparrowgate Petals</span></div>
  <div class="social" aria-label="Social links"><span></span><span></span><span></span><span></span></div>
</footer>
<div class="copy">©2024 Sparrowgate Petals. All Rights Reserved.</div>

</body>
</html>
```